Medical Device Company- Ankle Brace package

We need help redesigning our ankle brace product bag. We've attached a previous version of it that includes our old company name (bright path medical) and the color teal as an accent, which we are not using anymore. We prefer the package color to be in the dark grey but we are open to other colors such as black, white, light grey and slate blue. We are looking for design elements, creativity and a better layout.
- New Company Name = Velmirax
- Package Size 11 inches x 8.5 inches.
- We do not need sizing on the bag but need a spot to place a sticker.
Industry/Entity Type
medical devices
Look and feel

```html
<!DOCTYPE html>
<html lang="en">
<head>
<meta charset="utf-8">
<title>Velmirax Ankle Brace Package</title>
<link rel="stylesheet" href="https://fonts.googleapis.com/css2?family=Saira+Semi+Condensed:wght@500;600;700&display=swap">
<style>
  :root {
    --backdrop: #2a2c2f;
    --slate-dark: #2f4352;
    --slate-title: #3b4f60;
    --panel-top: #c9d4de;
    --panel-bottom: #8ea2b4;
    --seal-light: #d9e0e6;
    --band-light: #eef2f5;
    --pill-bg: #f4f6f8;
    --text-light: #f3f6f9;
    --brace-dark: #1f2226;
    --sock-white: #e6e9eb;
  }
  * { box-sizing: border-box; margin: 0; padding: 0; }
  html, body { width: 1200px; height: 1200px; overflow: hidden; }
  body {
    background: var(--backdrop);
    font-family: "Saira Semi Condensed", "Arial Narrow", sans-serif;
    position: relative;
  }
  .package {
    position: absolute;
    left: 240px; top: 135px;
    width: 720px; height: 930px;
    overflow: hidden;
    border-radius: 6px;
    background: linear-gradient(180deg, var(--panel-top) 0%, var(--panel-bottom) 100%);
    box-shadow: 0 20px 50px rgba(0,0,0,.45);
  }
  .seal {
    position: absolute; left: 0; top: 0; width: 100%; height: 60px;
    background: linear-gradient(180deg, #c3ccd4 0%, var(--seal-light) 100%);
  }
  .top-band {
    position: absolute; left: 0; top: 60px; width: 100%; height: 80px;
    background: var(--slate-dark);
  }
  .logo-band {
    position: absolute; left: 0; top: 140px; width: 100%; height: 120px;
    background: linear-gradient(180deg, var(--band-light) 0%, #d2dbe3 100%);
  }
  .brand {
    position: absolute; left: 60px; top: 178px;
    display: flex; align-items: center; gap: 14px;
    color: var(--slate-dark); font-weight: 600; font-size: 44px; line-height: 1;
  }
  .brand .brand-mark { width: 40px; height: 40px; background: var(--slate-dark); }
  .product-photo {
    position: absolute; left: 420px; top: 300px; width: 270px; height: 580px;
    border-radius: 12px;
    background: linear-gradient(180deg, var(--brace-dark) 0%, #2c3035 70%, var(--sock-white) 100%);
  }
  .title {
    position: absolute; left: 60px; top: 300px;
    color: var(--slate-title); font-weight: 600;
    font-size: 96px; line-height: .9; letter-spacing: 1px;
    text-transform: uppercase;
  }
  .feature-pill {
    position: absolute; left: 64px; top: 490px;
    padding: 4px 16px;
    background: var(--pill-bg); border-radius: 8px;
    color: var(--slate-dark); font-weight: 600; font-size: 28px; letter-spacing: .5px;
    text-transform: uppercase;
  }
  .contents {
    position: absolute; left: 70px; top: 548px;
    color: var(--text-light); font-weight: 500; font-size: 24px;
  }
  .approval {
    position: absolute; left: 60px; top: 700px;
    display: flex; align-items: center;
  }
  .approval .seal-badge {
    width: 80px; height: 80px; border-radius: 50%;
    background: radial-gradient(circle, #e9edf1 0%, #b6c2cd 100%);
    border: 3px solid #dfe5ea;
    position: relative; z-index: 1;
    box-shadow: 0 2px 6px rgba(0,0,0,.25);
  }
  .approval .approval-text {
    margin-left: -20px; padding: 8px 18px 8px 32px;
    background: rgba(222,229,235,.9); border-radius: 0 8px 8px 0;
    color: var(--slate-dark); line-height: 1.15;
  }
  .approval .approval-label { font-size: 13px; font-weight: 600; }
  .approval .approval-body { font-size: 18px; font-weight: 500; }
</style>
</head>
<body>
  <main class="package">
    <div class="seal"></div>
    <div class="top-band"></div>
    <div class="logo-band"></div>
    <div class="brand"><span class="brand-mark"></span><span>Velmirax</span></div>

    <div class="product-photo" role="img" aria-label="Photo of a black compression ankle brace with crossing strap worn over a white sock"></div>

    <h1 class="title">Ankle<br>Brace</h1>
    <div class="feature-pill">With Compression</div>
    <p class="contents">1 Brace and 1 Strap</p>

    <div class="approval">
      <div class="seal-badge"></div>
      <div class="approval-text">
        <div class="approval-label">Approved By</div>
        <div class="approval-body">An Orthopaedic<br>Surgeon And Podiatrist</div>
      </div>
    </div>
  </main>
</body>
</html>
```